Infographic for a Life Transformation brand to showcase their principle method

I need a clean infographic which would be used in a brochure to show the 5 steps to achieving a Quiet Harvest. (ie Life transformation). I use the theme of a revolution so I would like the graphic to include a raised fist or something to represent a revolution and then the 5 points of information to represent each step.
Needs to very clean and simple. I don't want something that would take up a full page, I want it as a graphic, almost like a big logo. I don't want it laid out like a process chart.

My brand personalities from https://tonequirkhub.com.au/ are
The Everyman and The Magician to give you an idea of my brand.

I've attached my logo so that you can see the colour of it. Graphic doesn't need to match logo but should align with that colour.

Target Market(s)

Top Tier Executives, males, 35-55y old

Industry/Entity Type

Life Coaching

Requirements
Must have
• The graphic must have the 5 Steps: in this order
1.Clarity
2. Measurement
3. Discipline
4. Nutrition
5.Exercise
Nice to have
• It could include these action steps which line up with the 5 steps, It may be too much information by there is the option to include if it works.
1.see it
2. track it
3. do it
4. eat it
5. move it

```html
<!DOCTYPE html>
<html lang="en">
<head>
<meta charset="utf-8">
<title>Five Steps to a Quiet Harvest</title>
<link rel="stylesheet" href="https://fonts.googleapis.com/css2?family=Poppins:ital,wght@1,700;1,800&display=swap">
<style>
  :root {
    --brand-blue: #0b4f91;
    --paper: #ffffff;
  }
  html, body {
    margin: 0;
    padding: 0;
    width: 1200px;
    height: 919px;
    overflow: hidden;
    background: var(--paper);
  }
  .infographic {
    display: block;
    width: 1200px;
    height: 919px;
  }
  .step-number {
    font-family: "Poppins", sans-serif;
    font-style: italic;
    font-weight: 800;
    font-size: 290px;
    fill: var(--brand-blue);
    stroke: var(--paper);
    stroke-width: 10px;
    paint-order: stroke;
  }
  .step-frame {
    fill: var(--paper);
    stroke: var(--brand-blue);
    stroke-width: 4px;
  }
  .step-title {
    font-family: "Poppins", sans-serif;
    font-style: italic;
    font-weight: 700;
    font-size: 64px;
    fill: var(--brand-blue);
  }
  .action-band {
    fill: var(--brand-blue);
  }
  .action-label {
    font-family: "Poppins", sans-serif;
    font-style: italic;
    font-weight: 700;
    font-size: 112px;
    fill: var(--paper);
  }
</style>
</head>
<body>
<svg class="infographic" viewBox="0 0 2200 1685" preserveAspectRatio="none" xmlns="http://www.w3.org/2000/svg">
  <defs>
    <linearGradient id="fist-tone" x1="0" y1="0" x2="0" y2="1">
      <stop offset="0" stop-color="#0b4f91" stop-opacity="0.35"/>
      <stop offset="1" stop-color="#0b4f91" stop-opacity="0.18"/>
    </linearGradient>
  </defs>

  <!-- Central emblem -->
  <rect class="emblem-area" role="img" aria-label="Raised fist symbolising revolution, drawn in brand blue" x="790" y="555" width="615" height="1130" rx="60" fill="url(#fist-tone)"/>

  <!-- Step 1 -->
  <g class="step step-clarity">
    <polygon class="step-frame" points="370,1061 755,1061 735,1180 350,1180"/>
    <text class="step-title" x="395" y="1146" textLength="317" lengthAdjust="spacingAndGlyphs">CLARITY</text>
    <polygon class="action-band" points="221,1176 604,1180 585,1286 201,1286"/>
    <text class="action-label" x="240" y="1270" textLength="330" lengthAdjust="spacingAndGlyphs">SEE IT</text>
    <text class="step-number" x="262" y="1175">1</text>
  </g>

  <!-- Step 2 -->
  <g class="step step-measurement">
    <polygon class="step-frame" points="250,563 845,563 825,676 240,676"/>
    <text class="step-title" x="293" y="641" textLength="510" lengthAdjust="spacingAndGlyphs">MEASUREMENT</text>
    <polygon class="action-band" points="78,672 645,676 627,782 58,782"/>
    <text class="action-label" x="105" y="766" textLength="502" lengthAdjust="spacingAndGlyphs">TRACK IT</text>
    <text class="step-number" x="100" y="668">2</text>
  </g>

  <!-- Step 3 -->
  <g class="step step-discipline">
    <polygon class="step-frame" points="1140,228 1575,228 1550,342 1125,337"/>
    <text class="step-title" x="1170" y="308" textLength="368" lengthAdjust="spacingAndGlyphs">DISCIPLINE</text>
    <polygon class="action-band" points="942,337 1365,342 1345,447 920,447"/>
    <text class="action-label" x="985" y="432" textLength="300" lengthAdjust="spacingAndGlyphs">DO IT</text>
    <text class="step-number" x="988" y="334">3</text>
  </g>

  <!-- Step 4 -->
  <g class="step step-nutrition">
    <polygon class="step-frame" points="1705,563 2135,563 2108,676 1690,676"/>
    <text class="step-title" x="1733" y="641" textLength="359" lengthAdjust="spacingAndGlyphs">NUTRITION</text>
    <polygon class="action-band" points="1503,672 1913,676 1895,782 1483,782"/>
    <text class="action-label" x="1535" y="766" textLength="325" lengthAdjust="spacingAndGlyphs">EAT IT</text>
    <text class="step-number" x="1540" y="668">4</text>
  </g>

  <!-- Step 5 -->
  <g class="step step-exercise">
    <polygon class="step-frame" points="1650,1062 2090,1062 2065,1175 1630,1175"/>
    <text class="step-title" x="1683" y="1147" textLength="365" lengthAdjust="spacingAndGlyphs">EXERCISE</text>
    <polygon class="action-band" points="1458,1174 1988,1175 1968,1283 1438,1283"/>
    <text class="action-label" x="1475" y="1267" textLength="473" lengthAdjust="spacingAndGlyphs">MOVE IT</text>
    <text class="step-number" x="1495" y="1173">5</text>
  </g>
</svg>
</body>
</html>
```